Orvane Yuletide Pageant 2025

We’re looking for a designer to help refresh the visual identity of our annual Christmas show while maintaining continuity from previous years. The updated design should feel festive, and warm, with a sense of celebration and anticipation. We’d like a central graphic that can be adapted for posters, social media, and digital signage, along with supporting assets for flyers and banners.

We’re open to seasonal color palettes such as rich reds, deep greens or blues, golds, silvers, or cool winter tones, and prefer typography that’s clear and elegant. The overall look should feel familiar to returning audiences while inviting and engaging for newcomers.

Two key groups: the current attenders of our congregation and the broader community in our suburb of Rochester, NY. Our congregation is made up of families, older adults, and young professionals who value faith, community and spiritual growth. The surrounding community is a fast growing friendly and family-oriented area of young professionals and longtime families.

We’re looking for a designer to help refresh the visual identity of our annual Christmas show while maintaining continuity with the theme and tone of previous years. The updated design should feel festive, and warm, with a sense of celebration and anticipation. We’d like a central graphic that can be adapted for posters, social media, and digital signage, along with supporting assets for flyers and banners.

Target Market(s)

Two key groups: the current attenders of our congregation and the broader community in our suburb of Rochester, NY. Our congregation is made up of families, older adults, and young professionals who value faith, community and spiritual growth. The surrounding community is a fast growing friendly and family-oriented area of young professionals and long time families.

Industry/Entity Type

Non-profit. Church

Font styles to use
Serif
Decorative
Script
Other font styles liked:
• Quentin

Requirements
Must have
• Sparkle, eye catching
Should not have
• must not look identical to the uploaded versions

```html
<!DOCTYPE html>
<html lang="en">
<head>
<meta charset="utf-8">
<title>Orvane Yuletide Pageant – Banner Options</title>
<link rel="stylesheet" href="https://fonts.googleapis.com/css2?family=Bodoni+Moda:wght@500&family=Marcellus&family=Montserrat:wght@700&family=Great+Vibes&display=swap">
<style>
  :root{
    --board:#ffffff;
    --ink:#111111;
    --cream:#fbefe2;
    --peach:#efc7a4;
    --gold-line:#d7b18b;
    --gold-glow:rgba(226,186,145,.55);
    --gold-soft:rgba(226,186,145,.22);
    --pine-dark:#3b5c41;
    --pine-mid:#557a58;
    --pine-light:#6f9471;
    --pine-flap:#416747;
    --wine-dark:#561519;
    --wine-mid:#7c2229;
    --wine-light:#a65a5e;
    --seal:#d4a236;
    --seal-light:#f6da86;
  }
  *{margin:0;padding:0;box-sizing:border-box}
  html,body{width:1200px;height:410px;overflow:hidden;background:var(--board)}
  .board{position:relative;width:1200px;height:410px}

  .option{position:absolute;top:55px;width:538px;height:302px;overflow:hidden}
  .option--pine{left:44px;
    background:
      radial-gradient(ellipse 170px 100px at 28% 45%, var(--pine-light), transparent 70%),
      radial-gradient(ellipse 180px 90px at 70% 62%, var(--pine-light), transparent 70%),
      radial-gradient(ellipse 170px 110px at 88% 22%, var(--pine-dark), transparent 70%),
      radial-gradient(ellipse 150px 90px at 12% 90%, var(--pine-dark), transparent 70%),
      var(--pine-mid);}
  .option--wine{left:619px;
    background:linear-gradient(110deg, var(--wine-light) 0%, var(--wine-dark) 22%, var(--wine-mid) 50%, var(--wine-light) 66%, var(--wine-mid) 80%, var(--wine-dark) 92%, var(--wine-light) 100%);}

  .option-label{position:absolute;top:368px;width:538px;text-align:center;
    font:700 7.5px/1 "Montserrat",sans-serif;letter-spacing:.08em;color:var(--ink)}
  .option-label--pine{left:44px}
  .option-label--wine{left:619px}

  .flap{position:absolute;inset:0}

  /* corner frames with filigree fill */
  .corner{position:absolute;width:78px;height:78px;border-color:var(--gold-line);border-style:solid;border-width:0}
  .corner--tl{top:20px;left:20px;border-top-width:1px;border-left-width:1px;
    background:radial-gradient(circle at 0 0, var(--gold-glow), var(--gold-soft) 40%, transparent 72%)}
  .corner--tr{top:20px;right:20px;border-top-width:1px;border-right-width:1px;
    background:radial-gradient(circle at 100% 0, var(--gold-glow), var(--gold-soft) 40%, transparent 72%)}
  .corner--bl{bottom:20px;left:20px;border-bottom-width:1px;border-left-width:1px;
    background:radial-gradient(circle at 0 100%, var(--gold-glow), var(--gold-soft) 40%, transparent 72%)}
  .corner--br{bottom:20px;right:20px;border-bottom-width:1px;border-right-width:1px;
    background:radial-gradient(circle at 100% 100%, var(--gold-glow), var(--gold-soft) 40%, transparent 72%)}

  .burst{position:absolute;border-radius:50%;
    background:radial-gradient(circle, rgba(246,214,178,.9) 0 4%, rgba(232,190,148,.55) 12%, rgba(226,186,145,.25) 45%, rgba(226,186,145,0) 70%)}

  .stars{position:absolute;width:30px;height:24px;overflow:visible}
  .stars path{fill:var(--peach)}
  .stars circle{fill:var(--cream)}

  .flourish{position:absolute;border-radius:50%;
    background:radial-gradient(ellipse, rgba(240,205,170,.34), rgba(240,205,170,.12) 50%, rgba(240,205,170,0) 72%)}

  .host{position:absolute;left:0;right:0;top:19px;text-align:center;
    font:700 7.6px/1 "Montserrat",sans-serif;letter-spacing:.06em;color:var(--peach)}
  .presents{position:absolute;left:0;right:0;top:30px;text-align:center;
    font:400 7.6px/1 "Marcellus",serif;letter-spacing:.12em;color:var(--peach)}

  .title{position:absolute;inset:0;color:var(--cream);font-weight:normal}
  .title-line{position:absolute;left:0;right:0;text-align:center;font-family:"Bodoni Moda",serif;font-weight:500;line-height:1;letter-spacing:.04em}
  .title-line--accent{background:linear-gradient(90deg,#fff6ec 10%,var(--peach) 90%);-webkit-background-clip:text;background-clip:text;color:transparent}
  .title-script{position:absolute;left:0;right:0;text-align:center;font-family:"Great Vibes",cursive;line-height:1;color:var(--cream)}

  .option--pine .title-line--top{top:45px;font-size:31px}
  .option--pine .title-line--accent{top:79px;font-size:43px}
  .option--pine .title-script{top:120px;font-size:54px}

  .option--wine .title-line--top{top:66px;font-size:36px}
  .option--wine .title-line--accent{top:105px;font-size:53px}
  .option--wine .title-script{top:154px;font-size:66px}

  .date{position:absolute;left:0;right:0;bottom:18px;text-align:center;color:var(--peach)}
  .date-day{font:400 12.5px/1 "Marcellus",serif;letter-spacing:.03em}
  .date-time{font:700 12.5px/1 "Montserrat",sans-serif;letter-spacing:.06em;margin-left:4px}

  .seal{position:absolute;left:238px;top:206px;width:61px;height:59px;border-radius:48% 52% 50% 50%;
    background:radial-gradient(circle at 40% 35%, var(--seal-light), var(--seal) 62%, #b07e22 100%);
    box-shadow:0 2px 4px rgba(0,0,0,.25)}
</style>
</head>
<body>
<main class="board">

  <section class="option option--pine" aria-label="Banner option 1, green">
    <svg class="flap" viewBox="0 0 538 302" aria-hidden="true">
      <polygon points="0,180 269,237 538,180 538,302 0,302" fill="var(--pine-flap)" opacity=".55"/>
      <polyline points="0,180 269,237 538,180" fill="none" stroke="#2f4d35" stroke-width="1.5" opacity=".6"/>
    </svg>

    <div class="corner corner--tl" role="img" aria-label="Gold filigree corner ornament"></div>
    <div class="corner corner--tr" role="img" aria-label="Gold filigree corner ornament"></div>
    <div class="corner corner--bl" role="img" aria-label="Gold filigree corner ornament"></div>
    <div class="corner corner--br" role="img" aria-label="Gold filigree corner ornament"></div>

    <div class="burst" role="img" aria-label="Gold firework burst" style="left:38px;top:64px;width:72px;height:72px"></div>
    <div class="burst" role="img" aria-label="Gold firework burst" style="left:443px;top:114px;width:62px;height:62px"></div>

    <svg class="stars" viewBox="0 0 30 24" style="left:106px;top:54px" aria-hidden="true">
      <circle cx="9" cy="4" r="1.2"/><circle cx="14" cy="6" r="1"/><circle cx="4" cy="10" r="1"/><circle cx="10" cy="11" r="1.3"/>
      <path d="M22 10l1.6 3.6 3.9.3-3 2.5.9 3.8L22 18.2l-3.4 2 .9-3.8-3-2.5 3.9-.3z"/>
    </svg>
    <svg class="stars" viewBox="0 0 30 24" style="left:422px;top:220px" aria-hidden="true">
      <circle cx="9" cy="4" r="1.2"/><circle cx="14" cy="6" r="1"/><circle cx="4" cy="10" r="1"/><circle cx="10" cy="11" r="1.3"/>
      <path d="M22 10l1.6 3.6 3.9.3-3 2.5.9 3.8L22 18.2l-3.4 2 .9-3.8-3-2.5 3.9-.3z"/>
    </svg>

    <div class="flourish" role="img" aria-label="Calligraphic flourish, left wing" style="left:126px;top:60px;width:90px;height:150px"></div>
    <div class="flourish" role="img" aria-label="Calligraphic flourish, right wing" style="left:330px;top:60px;width:90px;height:150px"></div>
    <div class="flourish" role="img" aria-label="Calligraphic flourish band beneath the title" style="left:170px;top:176px;width:200px;height:50px"></div>

    <p class="host">MAPLE HOLLOW COMMUNITY CHURCH</p>
    <p class="presents">PRESENTS</p>
    <h1 class="title">
      <span class="title-line title-line--top">ORVANE</span>
      <span class="title-line title-line--accent">YULETIDE</span>
      <span class="title-script">Pageant</span>
    </h1>

    <div class="seal" role="img" aria-label="Gold wax seal with star"></div>

    <p class="date"><span class="date-day">DEC 16 &amp; 17</span><span class="date-time">6:00 PM</span></p>
  </section>
  <p class="option-label option-label--pine">OPTION 1</p>

  <section class="option option--wine" aria-label="Banner option 2, red">
    <div class="corner corner--tl" role="img" aria-label="Gold filigree corner ornament"></div>
    <div class="corner corner--tr" role="img" aria-label="Gold filigree corner ornament"></div>
    <div class="corner corner--bl" role="img" aria-label="Gold filigree corner ornament"></div>
    <div class="corner corner--br" role="img" aria-label="Gold filigree corner ornament"></div>

    <div class="burst" role="img" aria-label="Gold firework burst" style="left:20px;top:110px;width:70px;height:70px"></div>
    <div class="burst" role="img" aria-label="Gold firework burst" style="left:448px;top:124px;width:64px;height:64px"></div>

    <svg class="stars" viewBox="0 0 30 24" style="left:94px;top:58px" aria-hidden="true">
      <circle cx="9" cy="4" r="1.2"/><circle cx="14" cy="6" r="1"/><circle cx="4" cy="10" r="1"/><circle cx="10" cy="11" r="1.3"/>
      <path d="M22 10l1.6 3.6 3.9.3-3 2.5.9 3.8L22 18.2l-3.4 2 .9-3.8-3-2.5 3.9-.3z"/>
    </svg>
    <svg class="stars" viewBox="0 0 30 24" style="left:424px;top:204px" aria-hidden="true">
      <circle cx="9" cy="4" r="1.2"/><circle cx="14" cy="6" r="1"/><circle cx="4" cy="10" r="1"/><circle cx="10" cy="11" r="1.3"/>
      <path d="M22 10l1.6 3.6 3.9.3-3 2.5.9 3.8L22 18.2l-3.4 2 .9-3.8-3-2.5 3.9-.3z"/>
    </svg>

    <div class="flourish" role="img" aria-label="Calligraphic flourish, left wing" style="left:80px;top:80px;width:110px;height:180px"></div>
    <div class="flourish" role="img" aria-label="Calligraphic flourish, right wing" style="left:350px;top:80px;width:110px;height:180px"></div>
    <div class="flourish" role="img" aria-label="Calligraphic flourish band beneath the title" style="left:140px;top:222px;width:260px;height:56px"></div>

    <p class="host">MAPLE HOLLOW COMMUNITY CHURCH</p>
    <p class="presents">PRESENTS</p>
    <h2 class="title">
      <span class="title-line title-line--top">ORVANE</span>
      <span class="title-line title-line--accent">YULETIDE</span>
      <span class="title-script">Pageant</span>
    </h2>

    <p class="date"><span class="date-day">DEC 16 &amp; 17</span><span class="date-time">6:00 PM</span></p>
  </section>
  <p class="option-label option-label--wine">OPTION 2</p>

</main>
</body>
</html>
```